The Lantern Harbor Summit (Poster or Color Flyer)

Unique and not too traditional design with Wording:
The Lantern Harbor Summit: The Deeper Message of God's Relentless Love
Friday Aug. 5 - Sunday the 7th
Denver 2016
www.TheLanternSummit.example
Updates
Project Deadline Extended
Reason: Our first experience with this type of design service was with 47Pixel, and we received 140 designs within a week.
We received only 2 designers submissions by our first 5 days with Mosaic Bench. We received an email that our time would be extended, which is much appreciated. The last 24 hours has brought in several new designs - which is great. However, we have a team of reviewers on our end - and due to Christmas break, will not be able to make a decision until January 4 or 5.
Can our deadline be moved to January 5? (at no charge?)
THANKS,
Trevor
Target Market(s)
General public. Professors. Pastors.
Requirements
Must have
- Basic info above.
Nice to have
- Subtle verses tucked into the graphics
- See www.TheQKTs.example for some of these,
- such as Romans 11:32, 1 John 2:2, 1 Timothy 4:10, John 12:32
Should not have
- Typical religious appearance.

```html
<!DOCTYPE html>
<html lang="en">
<head>
<meta charset="utf-8">
<title>The Lantern Harbor Summit</title>
<link href="https://fonts.googleapis.com/css2?family=Alegreya:wght@400;700;800&display=swap" rel="stylesheet">
<style>
  :root {
    --cream: #fffbe6;
    --sun: #fbf06a;
    --amber: #f3b62b;
    --title-red: #e8141c;
    --deep-red: #e3101a;
    --dot-gold: #e9a93a;
    --verse: rgba(170, 165, 60, 0.28);
    --verse-ref: rgba(165, 150, 60, 0.35);
    --lime: #e0ec86;
  }
  * { margin: 0; padding: 0; box-sizing: border-box; }
  html, body { width: 848px; height: 1200px; overflow: hidden; }
  body { font-family: "Alegreya", Georgia, serif; }
  .poster {
    position: relative;
    width: 848px;
    height: 1200px;
    overflow: hidden;
    background:
      radial-gradient(ellipse 70% 45% at 50% 30%, var(--cream) 0%, rgba(255,251,230,0) 70%),
      linear-gradient(180deg, #fffaf0 0%, #fdf6c4 35%, var(--sun) 58%, var(--amber) 82%, #e8721c 100%);
  }
  .figure-art {
    position: absolute;
    left: 80px;
    top: 270px;
    width: 700px;
    height: 760px;
    background: radial-gradient(ellipse 45% 55% at 50% 55%, rgba(240,150,60,0.85) 0%, rgba(238,110,40,0.6) 45%, rgba(240,60,30,0) 75%);
  }
  .title {
    position: absolute;
    top: 46px;
    left: 0;
    width: 100%;
    text-align: center;
    color: var(--title-red);
    font-weight: 800;
    font-size: 64px;
    line-height: 78px;
    letter-spacing: 1px;
  }
  .divider-dots {
    position: absolute;
    top: 200px;
    left: 24px;
    width: 800px;
    height: 12px;
  }
  .subtitle {
    position: absolute;
    top: 228px;
    left: 0;
    width: 100%;
    text-align: center;
    color: var(--title-red);
    font-weight: 800;
    font-size: 25px;
    letter-spacing: 0.3px;
  }
  .verses {
    position: absolute;
    top: 286px;
    left: 42px;
    width: 756px;
    color: var(--verse);
    font-weight: 700;
    text-transform: uppercase;
  }
  .verse { margin-bottom: 22px; }
  .verse-text {
    font-size: 31px;
    line-height: 44.5px;
    text-align: justify;
    text-align-last: left;
  }
  .verse-ref {
    color: var(--verse-ref);
    font-size: 16px;
    text-align: right;
    margin-top: -20px;
    padding-right: 12px;
  }
  .dome {
    position: absolute;
    left: 0;
    top: 910px;
    width: 848px;
    height: 290px;
  }
  .details {
    position: absolute;
    top: 1008px;
    left: 0;
    width: 100%;
    text-align: center;
    color: var(--lime);
    font-size: 36px;
    line-height: 52px;
  }
  .details sup { font-size: 20px; vertical-align: 14px; line-height: 0; }
  .rule {
    position: absolute;
    top: 1120px;
    left: 140px;
    width: 560px;
    height: 1px;
    background: var(--lime);
  }
  .website {
    position: absolute;
    top: 1138px;
    left: 0;
    width: 100%;
    text-align: center;
    color: var(--lime);
    font-size: 22px;
    letter-spacing: 0.5px;
  }
</style>
</head>
<body>
<main class="poster">
  <div class="figure-art" role="img" aria-label="Glowing translucent figure of a man with arms open, looking upward, in warm orange to red tones"></div>

  <h1 class="title">THE LANTERN<br>HARBOR SUMMIT:</h1>

  <svg class="divider-dots" viewBox="0 0 800 12" aria-hidden="true">
    <defs>
      <pattern id="dot-row" width="16" height="12" patternUnits="userSpaceOnUse">
        <circle cx="8" cy="6" r="3.6" fill="#e9a93a"/>
      </pattern>
      <linearGradient id="dot-fade" x1="0" x2="1">
        <stop offset="0" stop-color="#fff" stop-opacity="0.2"/>
        <stop offset="0.12" stop-color="#fff" stop-opacity="1"/>
        <stop offset="0.88" stop-color="#fff" stop-opacity="1"/>
        <stop offset="1" stop-color="#fff" stop-opacity="0.2"/>
      </linearGradient>
      <mask id="dot-mask"><rect width="800" height="12" fill="url(#dot-fade)"/></mask>
    </defs>
    <rect width="800" height="12" fill="url(#dot-row)" mask="url(#dot-mask)"/>
  </svg>

  <h2 class="subtitle">THE DEEPER MESSAGE OF GOD'S RELENTLESS LOVE</h2>

  <section class="verses">
    <div class="verse">
      <p class="verse-text">For God has consigned all to disobedience so that he may have mercy on them all.</p>
      <p class="verse-ref">Romans 11:32</p>
    </div>
    <div class="verse">
      <p class="verse-text">He is the atoning sacrifice for our sins, and not only for ours but also for the sins of the whole world.</p>
      <p class="verse-ref">1 John 2:2</p>
    </div>
    <div class="verse">
      <p class="verse-text">And we have seen and testify that the Father has sent his Son to be the Savior of the world.</p>
      <p class="verse-ref">John 12:32</p>
    </div>
    <div class="verse">
      <p class="verse-text">That is why we labor because we trust in the living God who is the Savior of all men, especially those who believe.</p>
      <p class="verse-ref">1 Timothy 4:10</p>
    </div>
  </section>

  <svg class="dome" viewBox="0 0 848 290" preserveAspectRatio="none" aria-hidden="true">
    <path d="M-40 290 L-40 120 Q424 -30 888 120 L888 290 Z" fill="#e6ec70"/>
    <path d="M-40 290 L-40 132 Q424 -14 888 132 L888 290 Z" fill="#e3101a"/>
  </svg>

  <div class="details">
    <p>FRIDAY AUG. 5 - SUNDAY THE 7<sup>th</sup></p>
    <p>DENVER 2016</p>
  </div>
  <div class="rule"></div>
  <p class="website">WWW.THELANTERNSUMMIT.EXAMPLE</p>
</main>
</body>
</html>
```